Convert Design into Adobe Ilustrator (Ai) File - Product Label

Convert the provided Graphic Design into an Adobe Illustrator (Ai) File for a Product Label. This Ai file needs to be fully editable, organised into logical layers and well structured. The text needs to be outlined for printing. This is for a POUCH DESIGN. The pouch dimensions file is attached. We'll share the details for the other side of the pouch if you are interested in accepting this project. Thanks.

Industry/Entity Type

FOOD SUPPLEMENTS

```html
<!DOCTYPE html>
<html lang="en">
<head>
<meta charset="utf-8">
<title>Tidewell – Marine Collagen Complex Pouch Front</title>
<link href="https://fonts.googleapis.com/css2?family=Cormorant+Garamond:wght@400;500;600&display=swap" rel="stylesheet">
<style>
  :root {
    --page: #f2f1ee;
    --pouch-navy: #2a3557;
    --pouch-navy-deep: #252f4e;
    --gold: #e2a878;
    --gold-soft: #c9956c;
    --ink-light: #ffffff;
    --dieline: #29abe2;
  }
  * { margin: 0; padding: 0; box-sizing: border-box; }
  html, body { width: 1200px; height: 912px; overflow: hidden; background: var(--page); }
  .pouch-front {
    position: absolute; left: 284px; top: 25px;
    width: 632px; height: 862px;
    background: var(--pouch-navy);
    border-radius: 16px;
    overflow: hidden;
    font-family: "Cormorant Garamond", serif;
    color: var(--ink-light);
  }
  .wave-field {
    position: absolute; left: 0; top: 540px; width: 632px; height: 322px;
    background: linear-gradient(180deg, rgba(42,53,87,0) 0%, rgba(201,149,108,0.07) 50%, rgba(37,47,78,0.25) 100%);
  }
  .dielines { position: absolute; inset: 0; width: 632px; height: 862px; }
  .brand-mark {
    position: absolute; top: 34px; left: 0; width: 100%;
    display: flex; justify-content: center; align-items: center; gap: 8px;
    font-size: 20px; font-weight: 500; color: var(--gold); line-height: 24px;
  }
  .brand-mark .dot { width: 10px; height: 10px; border: 1px solid var(--gold); border-radius: 50%; }
  .brand-name {
    position: absolute; left: 61px; width: 494px; top: 154px;
    text-align: center; font-weight: 500;
    font-size: 42px; letter-spacing: 1px; color: var(--gold); line-height: 48px;
  }
  .brand-rule { position: absolute; left: 61px; top: 216px; width: 494px; height: 2px; background: var(--gold-soft); }
  .product-title {
    position: absolute; left: 63px; top: 248px;
    font-size: 52px; font-weight: 500; line-height: 42px;
    color: var(--gold); letter-spacing: 1px;
  }
  .formula {
    position: absolute; left: 73px; top: 451px;
    font-size: 26px; font-weight: 500; line-height: 33.5px;
  }
  .servings { position: absolute; left: 73px; top: 575px; font-size: 15px; font-weight: 500; }
  .features { position: absolute; left: 346px; top: 447px; list-style: none; }
  .features li {
    display: flex; align-items: center; gap: 14px;
    height: 50px; font-size: 14px; font-weight: 500; line-height: 16px;
  }
  .features svg { width: 34px; height: 34px; flex: none; }
  .footer-note {
    position: absolute; left: 0; width: 100%; top: 827px;
    text-align: center; font-size: 15px; font-weight: 500;
  }
</style>
</head>
<body>
  <section class="pouch-front">
    <div class="wave-field" role="img" aria-label="Fine gold contour wave lines flowing across the lower pouch"></div>

    <svg class="dielines" viewBox="0 0 632 862" aria-hidden="true">
      <g fill="none" stroke="var(--dieline)" stroke-width="1.2" stroke-dasharray="5 4">
        <line x1="0" y1="105" x2="632" y2="105"/>
        <line x1="0" y1="125" x2="632" y2="125"/>
        <line x1="30" y1="0" x2="30" y2="862"/>
        <line x1="604" y1="0" x2="604" y2="862"/>
        <line x1="0" y1="679" x2="30" y2="679"/>
        <line x1="604" y1="679" x2="632" y2="679"/>
        <path d="M30 679 C 120 790, 220 828, 317 828 C 414 828, 514 790, 604 679"/>
      </g>
    </svg>

    <div class="brand-mark"><span class="dot"></span>Tidewell</div>

    <h1 class="brand-name">Tidewell</h1>
    <div class="brand-rule"></div>

    <h2 class="product-title">MARINE<br>COLLAGEN<br>COMPLEX</h2>

    <p class="formula">Marine Collagen,<br>Vitamin C<br>&amp; Hyaluronic Acid</p>
    <p class="servings">30 servings | 13.500mg per serving</p>

    <ul class="features">
      <li>
        <svg viewBox="0 0 32 32" fill="none" stroke="var(--gold)" stroke-width="1.4">
          <circle cx="16" cy="16" r="13"/><circle cx="16" cy="16" r="5"/>
        </svg>
        Low molecular weight
      </li>
      <li>
        <svg viewBox="0 0 32 32" fill="none" stroke="var(--gold)" stroke-width="1.4">
          <path d="M16 3 C 10 12, 8 16, 8 20 a8 8 0 0 0 16 0 C 24 16, 22 12, 16 3 Z"/>
        </svg>
        2000 kDa
      </li>
      <li>
        <svg viewBox="0 0 32 32" fill="none" stroke="var(--gold)" stroke-width="1.4">
          <path d="M6 26 C 6 12, 14 6, 27 5 C 26 18, 20 26, 6 26 Z"/><path d="M6 26 L 20 12"/>
        </svg>
        Unflavoured
      </li>
      <li>
        <svg viewBox="0 0 32 32" fill="none" stroke="var(--gold)" stroke-width="1.4">
          <path d="M4 22 q4 -3 8 0 t8 0 t8 0"/><path d="M4 27 q4 -3 8 0 t8 0 t8 0"/><circle cx="16" cy="12" r="5"/>
        </svg>
        Sourced from<br>wild caught fish
      </li>
    </ul>

    <p class="footer-note">Food Supplement | ℮ 375g</p>
  </section>
</body>
</html>
```